Harborline Ted's Chinese/Dim Sum Restaurant Menu

Harborline Ted's is a seafood-asian fusion restaurant featuring dim sum and other classical asian fusion items.

We need a menu design that includes both our food menu and our drink menu.

Food menu: Needs to have space for descriptions of food (please just include a place holder and we will input them later). See attached for food menu items.

Drink menu: Just lists of items with prices. See attached Jade Pavilion Menu- please include the same items, but rebrand for Harborline Ted's.

The menus must be able to be printed in a 4.25x11in paper.

We want something modern and contemporary. My boss likes geometrical design aspects and minimalism. So, nothing too ornate. But, it has to be different from the Jade Pavilion menus. Colors can be black, red, gold or blue- but it must be able to be tied into our black and red Harborline Ted's logo. Including elements of Chinese culture, especially fishing, is a plus, but not necessary.

We also need this in ai format when we download final copy so we can edit in the future.

UPDATE: Please note, we already have a logo.

Target Market(s)

Upscale family diners

Industry/Entity Type

Chinese Food

Font styles to use
Serif
Sans Serif

Colors
0054AA
0677BA
7BADD7
CADEEF
E8F1F8
0094D4
00A9DD
6FCCEA
C7EBF8
E9F6FB
FFC000
F8CF3A
FAE287
FDF2CF
FEFAEE
EB3D1F
EC4F4E
F09395
F8D3D4
FCEDEE

Requirements
Must have
• Classic, minimalist, elegant

```html
<!DOCTYPE html>
<html lang="en">
<head>
<meta charset="utf-8">
<title>Harborline Ted's Menu</title>
<link href="https://fonts.googleapis.com/css2?family=Alegreya:wght@400;700;800&family=Arvo:wght@700&family=Montserrat:wght@500;700&display=swap" rel="stylesheet">
<style>
:root{
  --red:#da2a2a;
  --ink:#1c1c1c;
  --blue:#1f5fae;
  --paper:#ffffff;
  --backdrop:#2b2b2b;
  --serif:"Alegreya", Georgia, serif;
  --slab:"Arvo", Georgia, serif;
  --sans:"Montserrat", Arial, sans-serif;
}
*{box-sizing:border-box;margin:0;padding:0}
html,body{width:750px;height:1200px;overflow:hidden}
body{background:var(--backdrop);position:relative;font-family:var(--serif);color:var(--ink)}
.sheet{position:absolute;background:var(--paper)}
.sheet::before{content:"";position:absolute;inset:4px;border:0.6px dashed #444;pointer-events:none}
.order-sheet{top:49px;width:235px;height:609px}
.order-sheet.left{left:128px}
.order-sheet.right{left:386px}

.brand{display:flex;align-items:center;justify-content:center;gap:6px}
.brand-dot{width:9px;height:9px;border-radius:50%;background:var(--red)}
.brand-name{font-family:var(--sans);font-weight:700;letter-spacing:.3px;color:var(--ink);white-space:nowrap}
.order-sheet .brand{position:absolute;top:13px;left:0;right:0;height:100px}
.order-sheet .brand-name{font-size:16px}

.guest-fields{position:absolute;top:124px;left:15px;width:206px;font-weight:700;font-size:6px;line-height:11.5px}
.field-row{display:flex;gap:3px;white-space:nowrap}
.field-row span.line{flex:1;border-bottom:0.5px solid #333;height:8px}

.menu-tables{position:absolute;top:152px;left:15px;width:205px}
.order-table{width:205px;border-collapse:collapse;margin-bottom:11px;font-size:5.6px;table-layout:fixed}
.order-table col.qty{width:27px}
.order-table col.item{width:98px}
.order-table col.tag{width:49px}
.order-table col.price{width:31px}
.order-table th{background:var(--red);color:#fff;font-weight:700;height:9px;border:0.5px solid #444;letter-spacing:.3px;font-size:5.4px}
.order-table td{height:10.8px;border:0.5px solid #444;padding:0 2px;white-space:nowrap;overflow:hidden}
.order-table td.tag,.order-table td.price{text-align:center}
.spicy{color:var(--red)}
.gf{color:var(--blue)}

.spread{top:720px;height:433px}
.dessert-spread{left:32px;width:336px}
.bar-card{left:382px;width:335px}

.ribbon{position:absolute;height:13px;background:var(--red);color:#fff;font-family:var(--slab);font-weight:700;font-size:9.5px;letter-spacing:.4px;display:flex;align-items:center;justify-content:center;clip-path:polygon(0 0,100% 0,94% 50%,100% 100%,0 100%,6% 50%)}

.sweets-column{position:absolute;left:0;top:0;width:168px;height:100%;text-align:center}
.sweets-column .ribbon{left:32px;width:105px}
.dessert-list{position:absolute;top:61px;left:0;right:0}
.dessert{margin-bottom:7px}
.dessert h3{font-size:5px;font-weight:800;letter-spacing:.3px;line-height:6px}
.dessert p{font-size:5.2px;line-height:6px}
.price-red{color:var(--red);font-size:5px;font-weight:700;line-height:8px}
.na-list{position:absolute;top:251px;left:0;right:0}
.na-item{margin-bottom:7px}
.na-item p{font-size:5.2px;line-height:7px;letter-spacing:.2px}
.na-item small{display:block;font-size:3px;line-height:4px}

.happy-panel{position:absolute;left:168px;top:0;width:168px;height:100%;background:var(--red);color:#fff;text-align:center;font-family:var(--sans)}
.happy-panel .brand{position:absolute;top:128px;left:0;right:0}
.happy-panel .brand-name{color:#fff;font-size:14px}
.happy-panel .brand-dot{background:#fff}
.happy-title{position:absolute;top:202px;left:0;right:0;font-weight:500;font-size:8.6px}
.happy-time{position:absolute;top:215px;left:0;right:0;font-weight:500;font-size:6.3px}
.happy-ribbon{position:absolute;top:226px;left:32px;width:104px;height:12px;background:#fff;color:var(--red);font-weight:500;font-size:7px;display:flex;align-items:center;justify-content:center;clip-path:polygon(0 0,100% 0,94% 50%,100% 100%,0 100%,6% 50%)}
.happy-deals{position:absolute;top:242px;left:0;right:0;font-weight:500;font-size:5.4px;line-height:8px}
.fine-print{position:absolute;top:283px;left:34px;right:34px;font-size:4.2px;line-height:5px;font-weight:500}
.fine-print small{display:block;margin-top:4px;font-size:2.6px;line-height:3.4px}

.bar-card .brand{position:absolute;top:28px;left:0;right:0}
.bar-card .brand-name{font-size:10px}
.bar-card .brand-dot{width:6px;height:6px}
.bar-rule{position:absolute;top:52px;left:0;right:0;border-top:0.5px solid #999}
.bar-card .ribbon.one{left:31px;top:76px;width:110px}
.bar-card .ribbon.two{left:196px;top:76px;width:111px}
.cocktail{position:absolute;width:124px}
.cocktail.col-a{left:15px}
.cocktail.col-b{left:180px}
.cocktail h3{font-family:var(--slab);font-size:5.6px;line-height:6.4px;letter-spacing:.2px}
.cocktail p{font-size:4.5px;line-height:5.4px}
.cocktail .cost{position:absolute;top:0;right:-14px;color:var(--red);font-family:var(--slab);font-size:5.4px}
.bar-note{position:absolute;top:414px;left:0;right:0;text-align:center;color:var(--red);font-size:4.5px}
</style>
</head>
<body>

<section class="sheet order-sheet left">
  <div class="brand"><span class="brand-dot"></span><span class="brand-name">HARBORLINE TED'S</span></div>
  <div class="guest-fields">
    <div class="field-row">Table:<span class="line"></span>Guests:<span class="line" style="flex:1.6"></span></div>
    <div class="field-row">Name:<span class="line"></span>Email:<span class="line"></span></div>
  </div>
  <div class="menu-tables">
    <table class="order-table">
      <colgroup><col class="qty"><col class="item"><col class="tag"><col class="price"></colgroup>
      <tr><th>QTY</th><th>DIM SUM</th><th>V/Spicy /GF</th><th>Price</th></tr>
      <tr><td></td><td>1. Potsticker</td><td class="tag"></td><td class="price">$ 12</td></tr>
      <tr><td></td><td>2. Plantwise Dumpling</td><td class="tag">VEGAN</td><td class="price">$ 11</td></tr>
      <tr><td></td><td>3. Lobster Dumpling</td><td class="tag"></td><td class="price">$ 13</td></tr>
      <tr><td></td><td>4. Sticky Rice</td><td class="tag"></td><td class="price">$ 5</td></tr>
      <tr><td></td><td>5. Pork Siu Mai</td><td class="tag"></td><td class="price">$ 12</td></tr>
      <tr><td></td><td>6. Spicy Won Ton</td><td class="tag spicy">SPICY</td><td class="price">$ 12</td></tr>
      <tr><td></td><td>7. Vegan Spicy Won Ton</td><td class="tag">V/<span class="spicy">SP</span></td><td class="price">$ 12</td></tr>
      <tr><td></td><td>8. Pork Xie Long Boa</td><td class="tag"></td><td class="price">$ 11</td></tr>
      <tr><td></td><td>9. Crab &amp; Pork Xie Long Bao</td><td class="tag"></td><td class="price">$ 2</td></tr>
      <tr><td></td><td>10. BBQ Pork Bao</td><td class="tag"></td><td class="price">$ 10</td></tr>
      <tr><td></td><td>11. Sweet Corn Dumpling</td><td class="tag"></td><td class="price">$ 11</td></tr>
    </table>
    <table class="order-table">
      <colgroup><col class="qty"><col class="item"><col class="tag"><col class="price"></colgroup>
      <tr><th>QTY</th><th>SOUP</th><th>V/Spicy /GF</th><th>Price</th></tr>
      <tr><td></td><td>12. Cup Hot &amp; Sour Soup</td><td class="tag spicy">SPICY</td><td class="price">$ 5</td></tr>
      <tr><td></td><td>13. Bowl Hot &amp; Sour Soup</td><td class="tag spicy">SPICY</td><td class="price">$ 8</td></tr>
      <tr><td></td><td>14. Cup Egg Flower Soup</td><td class="tag"></td><td class="price">$ 5</td></tr>
      <tr><td></td><td>15. Bowl Egg Flower Soup</td><td class="tag"></td><td class="price">$ 8</td></tr>
      <tr><td></td><td>16. Bowl Pork Wonton Soup</td><td class="tag"></td><td class="price">$ 9</td></tr>
    </table>
    <table class="order-table">
      <colgroup><col class="qty"><col class="item"><col class="tag"><col class="price"></colgroup>
      <tr><th>QTY</th><th>APPETIZERS</th><th>V/Spicy /GF</th><th>Price</th></tr>
      <tr><td></td><td>17. Walnut Shrimp Warp</td><td class="tag gf">GF</td><td class="price">$ 12</td></tr>
      <tr><td></td><td>18. Chicken Lettuce Warp</td><td class="tag"></td><td class="price">$ 12</td></tr>
      <tr><td></td><td>19. Tofu Lettuce Warp</td><td class="tag">VEGAN</td><td class="price">$ 12</td></tr>
      <tr><td></td><td>20. Curry Mussels + add Noodles ($3)</td><td class="tag"></td><td class="price">$ 15</td></tr>
      <tr><td></td><td>21. Seabass Roll</td><td class="tag"></td><td class="price">$ 12</td></tr>
      <tr><td></td><td>22 Crab Cheese Wonton</td><td class="tag"></td><td class="price">$ 10</td></tr>
      <tr><td></td><td>23. Tuna Tower</td><td class="tag"></td><td class="price">$ 23</td></tr>
      <tr><td></td><td>24. Ahi Tuna and Fish Chips</td><td class="tag"></td><td class="price">$ 21</td></tr>
      <tr><td></td><td>25 Edamame</td><td class="tag">V/<span class="gf">GF</span></td><td class="price">$ 7</td></tr>
      <tr><td></td><td>26. Sesame Soy Noodle Salad (cold)</td><td class="tag">VEGAN</td><td class="price">$ 8</td></tr>
      <tr><td></td><td>27. Chinese Pancake</td><td class="tag">VEGAN</td><td class="price">$ 9</td></tr>
      <tr><td></td><td>28. Garlic Cucumber Salad</td><td class="tag">VEGAN</td><td class="price">$ 11</td></tr>
      <tr><td></td><td>29. Seaweed Salad</td><td class="tag">VEGAN</td><td class="price">$ 10</td></tr>
    </table>
    <table class="order-table">
      <colgroup><col class="qty"><col class="item"><col class="tag"><col class="price"></colgroup>
      <tr><th>QTY</th><th>SAUTEED</th><th>V/Spicy /GF</th><th>Price</th></tr>
      <tr><td></td><td>30. Szechuan Seabass</td><td class="tag"></td><td class="price">$ 18</td></tr>
      <tr><td></td><td>31. Seabass Black Bean Sauce</td><td class="tag"></td><td class="price">$ 18</td></tr>
      <tr><td></td><td>32. Kung Po Shrimp</td><td class="tag"><span class="spicy">SP</span>/<span class="gf">GF</span></td><td class="price">$ 20</td></tr>
      <tr><td></td><td>33. Kung Po Chicken</td><td class="tag spicy">SPICY</td><td class="price">$ 18</td></tr>
      <tr><td></td><td>34. Kung Po Tofu</td><td class="tag">V/<span class="spicy">SP</span>/<span class="gf">GF</span></td><td class="price">$ 18</td></tr>
    </table>
  </div>
</section>

<section class="sheet order-sheet right">
  <div class="brand"><span class="brand-dot"></span><span class="brand-name">HARBORLINE TED'S</span></div>
  <div class="guest-fields">
    <div class="field-row">Table:<span class="line"></span>Guests:<span class="line" style="flex:1.6"></span></div>
    <div class="field-row">Name:<span class="line"></span>Email:<span class="line"></span></div>
  </div>
  <div class="menu-tables">
    <table class="order-table">
      <colgroup><col class="qty"><col class="item"><col class="tag"><col class="price"></colgroup>
      <tr><th>QTY</th><th>SAUTEED</th><th>V/Spicy /GF</th><th>Price</th></tr>
      <tr><td></td><td>35. Broccoli Chicken</td><td class="tag"></td><td class="price">$ 18</td></tr>
      <tr><td></td><td>36. Broccoli Beef</td><td class="tag"></td><td class="price">$ 19</td></tr>
      <tr><td></td><td>37. Broccoli Shrimp</td><td class="tag gf">GF</td><td class="price">$ 20</td></tr>
      <tr><td></td><td>38. Mongolian Beef</td><td class="tag spicy">SPICY</td><td class="price">$ 20</td></tr>
      <tr><td></td><td>39. General Ng's Chicken</td><td class="tag spicy">SPICY</td><td class="price">$ 18</td></tr>
      <tr><td></td><td>40. General Ng's Tofu</td><td class="tag">V/<span class="spicy">SP</span></td><td class="price">$ 18</td></tr>
    </table>
    <table class="order-table">
      <colgroup><col class="qty"><col class="item"><col class="tag"><col class="price"></colgroup>
      <tr><th>QTY</th><th>VEGGIE</th><th>V/Spicy /GF</th><th>Price</th></tr>
      <tr><td></td><td>41. Sauteed Green Beans V/GF 16</td><td class="tag">V/<span class="gf">GF</span></td><td class="price">$ 16</td></tr>
      <tr><td></td><td>42. Iceberg Lettuce with "Oyster" Sauce</td><td class="tag">VEGAN</td><td class="price">$ 14</td></tr>
      <tr><td></td><td>43. Broccoli Garlic Sauce</td><td class="tag">V/<span class="gf">GF</span></td><td class="price">$ 15</td></tr>
    </table>
    <table class="order-table">
      <colgroup><col class="qty"><col class="item"><col class="tag"><col class="price"></colgroup>
      <tr><th>QTY</th><th>RICE &amp; NOODLES</th><th>V/Spicy /GF</th><th>Price</th></tr>
      <tr><td></td><td>44. Seafood Fried Rice</td><td class="tag"></td><td class="price">$ 18</td></tr>
      <tr><td></td><td>45. Veggie Fried Rice</td><td class="tag"></td><td class="price">$ 14</td></tr>
      <tr><td></td><td>46. Chicken Fried Rice</td><td class="tag"></td><td class="price">$ 15</td></tr>
      <tr><td></td><td>47. Beef Fried Rice</td><td class="tag"></td><td class="price">$ 16</td></tr>
      <tr><td></td><td>48. Seafood Chow Mein</td><td class="tag"></td><td class="price">$ 18</td></tr>
      <tr><td></td><td>49. Chicken Chow Mein</td><td class="tag"></td><td class="price">$ 16</td></tr>
      <tr><td></td><td>50. Beef Chow Mein</td><td class="tag"></td><td class="price">$ 17</td></tr>
    </table>
    <table class="order-table">
      <colgroup><col class="qty"><col class="item"><col class="tag"><col class="price"></colgroup>
      <tr><th>QTY</th><th>SWEET &amp; DESSER</th><th>V/Spicy /GF</th><th>Price</th></tr>
      <tr><td></td><td>51. Chocolate Dumpling 10</td><td class="tag"></td><td class="price">$ 10</td></tr>
      <tr><td></td><td>52. Sweet Egg Bao 9</td><td class="tag"></td><td class="price">$ 9</td></tr>
      <tr><td></td><td>53. Walnut Bao</td><td class="tag"></td><td class="price">$ 9</td></tr>
    </table>
  </div>
</section>

<section class="sheet spread dessert-spread">
  <div class="sweets-column">
    <div class="ribbon" style="top:39px">DESSERTS</div>
    <div class="dessert-list">
      <div class="dessert"><h3>PURE DECADENCE</h3><p>Molten Chocolate Lava Cake,<br>Pineapple Coconut Ice Cream,<br>Whipped Cream</p><div class="price-red">$9</div></div>
      <div class="dessert"><h3>CHEESECAKE</h3><div class="price-red">$8</div></div>
      <div class="dessert"><h3>PINEAPPLE COCONUT<br>ICE CREAM</h3><div class="price-red">$7</div></div>
      <div class="dessert"><h3>SALTED CARAMEL<br>ICE CREAM</h3><div class="price-red">$7</div></div>
      <div class="dessert"><h3>MARIONBERRY SORBET</h3><div class="price-red">$6</div></div>
      <div class="dessert"><h3>VANILLA ICE CREAM</h3><div class="price-red">$6</div></div>
    </div>
    <div class="ribbon" style="top:226px">NA BEVERAGES</div>
    <div class="na-list">
      <div class="na-item"><p>BOTTOMLESS - HOUSE COLA, DIET COLA,<br>COLA ZERO, LEMON-LIME, ROOT BEER,<br>CHERRY SPICE, GINGER ALE, TONIC<br>UNSWEETENED ICED TEA, LEMONADE</p><div class="price-red">$3</div></div>
      <div class="na-item"><p>APPLE, ORANGE, CRANBERRY,<br>GRAPEFRUIT, PINEAPPLE,<br>CHOCOLATE MILK, MILK</p><small>(NO REFILLS)</small><div class="price-red">$3</div></div>
      <div class="na-item"><p>VIRGIN PINA COLADA &amp;<br>VIRGIN STRAWBERRY DAQUIRI</p><small>(SHAKEN - NO REFILLS)</small><div class="price-red">$4.5</div></div>
      <div class="na-item"><p>STRAWBERRY LEMONADE, ROSY<br>TEMPLE, RED RANGER</p><small>(LIMIT ONE REFILL)</small><div class="price-red">$4</div></div>
    </div>
  </div>
  <div class="happy-panel">
    <div class="brand"><span class="brand-dot"></span><span class="brand-name">HARBORLINE TED'S</span></div>
    <div class="happy-title">HAPPY HOUR APPETIZERS*</div>
    <div class="happy-time">EVERYDAY 3 PM – 6 PM</div>
    <div class="happy-ribbon">DRINK &amp; APPETIZERS</div>
    <div class="happy-deals">$5 WELL LIQUORS<br>$1 OFF ALL ALCOHOLIC BEVERAGES</div>
    <div class="fine-print">*AVAILABLE ONLY IN THE BAR, DINE IN ONLY
      <small>JADE PAVILION RESTAURANT RESERVES THE RIGHT TO CHANGE MENU SELECTIONS, AND/OR THE PRICES THAT ACCOMPANY THOSE ITEMS, AS THEY APPEAR ON THE MENUS AT THE RESTAURANT.<br>ONLY ONE PROMOTION/SPECIAL/DISCOUNT/KICKBACK USED AT A TIME, PER TABLE OR CHECK<br>------------</small>
    </div>
  </div>
</section>

<section class="sheet spread bar-card">
  <div class="brand"><span class="brand-dot"></span><span class="brand-name">HARBORLINE TED'S</span></div>
  <div class="bar-rule"></div>
  <div class="ribbon one">COCKTAILS</div>
  <div class="ribbon two">COCKTAILS</div>

  <div class="cocktail col-a" style="top:103px"><h3>PINEAPPLE DAQUIRI</h3><p>Palmgrove Pineapple Rum, Lime Juice<br>Rich Simple Syrup</p><span class="cost">$12</span></div>
  <div class="cocktail col-a" style="top:135px"><h3>ELDERFLOWER GIMLET</h3><p>Alderwick Gin, St. Verdant<br>Elderflower Liqueur, Lime Juice</p><span class="cost">$12</span></div>
  <div class="cocktail col-a" style="top:171px"><h3>CEDAR ISLE<br>BLACKBERRY MANHATTAN</h3><p>Bramwell Whiskey, 98 pt. Cedar Isle<br>Blackberry Liqueur*, Aromatic Bitters</p><span class="cost">$14</span></div>
  <div class="cocktail col-a" style="top:212px"><h3>TED &amp; JIN</h3><p>Hollow Creek Whiskey, Alderwick Gin, Ginger Beer,<br>Orange Bitters, Lime Juice, Rosemary Simple Syrup</p><span class="cost">$13</span></div>
  <div class="cocktail col-a" style="top:250px"><h3>HI-YA MARGARITA</h3><p>Cienta Reposado, Triple Sec, Grand Orvelle, Lime Juice,<br>Rich Simple Syrup</p><span class="cost">$13</span></div>
  <div class="cocktail col-a" style="top:287px"><h3>CEDAR BRAMBLE</h3><p>Alderwick Gin, 98 pt. Cedar Isle Blackberry Liqueur*<br>Lemon Juice, Rich Simple Syrup</p><span class="cost">$13</span></div>
  <div class="cocktail col-a" style="top:324px"><h3>RUM PUNCH</h3><p>Maliko Coconut Rum, White Rum, Marlston Dark Rum<br>Orange Juice,<br>Pineapple Juice, Lime Juice,<br>Grenadine</p><span class="cost">$14</span></div>
  <div class="cocktail col-a" style="top:374px"><h3>BOURBON LEMONADE</h3><p>Knoll Ridge Bourbon, Lemon Juice, Mint<br>Simple Syrup</p><span class="cost">$13</span></div>

  <div class="cocktail col-b" style="top:103px"><h3>TEQUILA SMASH</h3><p>Hornera Reposado, Orvanne, Mint,<br>Lime Juice, Lemon Juice</p><span class="cost">$12</span></div>
  <div class="cocktail col-b" style="top:135px"><h3>MARLOW THE GOAT</h3><p>Tamsin Vodka, Cedar Isle Raspberry<br>Liqueur*, Ginger Beer, Fresh Lime</p><span class="cost">$13</span></div>
  <div class="cocktail col-b" style="top:168px"><h3>LAVENDER LOGANBERRY<br>LEMON DROP</h3><p>Citrus Vodka, 94 pt. Cedar Isle Loganberry<br>Liqueur*, Lemon Juice, Lavender Simple Syrup</p><span class="cost">$14</span></div>
  <div class="cocktail col-b" style="top:211px"><h3>NEW FASHIONED</h3><p>Bramwell Whiskey, Amaretto, Simple Syrup<br>Orange Bitters, Cherry, Orange</p><span class="cost">$14</span></div>
  <div class="cocktail col-b" style="top:247px"><h3>CEDAR ISLE<br>BLACKBERRY MANHATTAN</h3><p>Bramwell Whiskey, 98 pt. Cedar<br>Isle Blackberry Liqueur*,<br>Aromatic Bitters</p><span class="cost">$13</span></div>
  <div class="cocktail col-b" style="top:289px"><h3>CEDAR BRAMBLE</h3><p>Alderwick Gin, 98 pt. Cedar Isle Blackberry<br>Liqueur* Lemon Juice, Rich Simple Syrup</p><span class="cost">$12</span></div>
  <div class="cocktail col-b" style="top:328px"><h3>CHINATINI</h3><p>Citrus Vodka, Cedar Isle<br>Raspberry Liqueur*, Triple Sec, Cranberry Juice<br>Lemon Juice,<br>Rich Simple Syrup</p><span class="cost">$13</span></div>
  <div class="cocktail col-b" style="top:375px"><h3>SPIRIT FREE – SUMMER SUNSET</h3><p>Dawnline NA Orange<br>Pineapple Juice, Cranberry Juice, Orange Juice</p><span class="cost">$13</span></div>

  <p class="bar-note">* These cocktails use local Cedar Isle liquors or local ingredients</p>
</section>

</body>
</html>
```